Vorbly BIZ Card, email signature & Stationary

Professional business cards, email signatures and ms word letterhead

Target Market(s)

business owners

Industry/Entity Type

cloud hosting

Contact Information for Business Card

name title office phone number , direct line, fax email address web site

Font styles to use
Other font styles liked:
• something that compliments font in logo

```html
<!DOCTYPE html>
<html lang="en">
<head>
<meta charset="utf-8">
<title>Vorbly Stationery</title>
<link rel="stylesheet" href="https://fonts.googleapis.com/css2?family=Nunito:wght@300;400;600;800&display=swap">
<style>
  :root {
    --bg: #c0c0c0;
    --paper: #f8f8f8;
    --red: #ee1f2a;
    --ink: #111111;
    --white: #ffffff;
  }
  * { margin: 0; padding: 0; box-sizing: border-box; }
  html, body { width: 1200px; height: 952px; overflow: hidden; }
  body { background: var(--bg); font-family: "Nunito", sans-serif; color: var(--ink); position: relative; }

  .letterhead {
    position: absolute; left: 314px; top: 87px; width: 566px; height: 778px;
    background: var(--paper); box-shadow: 0 6px 18px rgba(0,0,0,.25);
  }
  .letterhead .brand {
    position: absolute; top: 36px; left: 0; width: 100%; text-align: center;
    font-size: 58px; font-weight: 300; color: var(--red); letter-spacing: -1px;
  }
  .letterhead .contacts {
    position: absolute; top: 736px; left: 0; width: 100%;
    display: flex; justify-content: center; gap: 28px; font-size: 10.5px; letter-spacing: .4px;
  }
  .contact-item { display: flex; align-items: center; gap: 5px; }
  .contact-item svg { width: 11px; height: 11px; fill: var(--red); }
  .letterhead .footer-band {
    position: absolute; left: 0; bottom: 0; width: 100%; height: 22px;
  }
  .footer-band svg { position: absolute; inset: 0; width: 100%; height: 100%; }
  .footer-band .address {
    position: relative; display: block; text-align: center; line-height: 22px;
    color: var(--white); font-size: 10px; letter-spacing: .4px; padding-right: 30px;
  }

  .card { position: absolute; left: 212px; width: 293px; height: 168px; box-shadow: 0 6px 14px rgba(0,0,0,.28); }
  .card-front { top: 304px; background: var(--red); }
  .card-front .brand {
    position: absolute; top: 0; left: 0; width: 100%; height: 100%;
    display: flex; align-items: center; justify-content: center;
    font-size: 48px; font-weight: 300; color: var(--white); letter-spacing: -1px;
  }
  .card-back { top: 487px; background: var(--paper); }
  .card-back .brand {
    position: absolute; left: 26px; top: 16px; font-size: 27px; font-weight: 300; color: var(--red); letter-spacing: -.5px;
  }
  .card-back .person { position: absolute; left: 197px; top: 20px; }
  .person .name { font-size: 11.5px; color: var(--red); font-weight: 400; }
  .person .name b { color: var(--ink); font-weight: 800; }
  .person .title { font-size: 6.5px; margin-top: 1px; }
  .card-back .address { position: absolute; left: 26px; top: 129px; font-size: 6.5px; line-height: 10px; }
  .card-back .details { position: absolute; left: 197px; top: 117px; font-size: 6.5px; }
  .card-back .details .contact-item { gap: 4px; height: 12px; }
  .card-back .details svg { width: 7px; height: 7px; }
  .card-back .band { position: absolute; left: 0; bottom: 0; width: 100%; height: 10px; }
</style>
</head>
<body>
  <svg width="0" height="0" style="position:absolute">
    <defs>
      <symbol id="icon-phone" viewBox="0 0 24 24"><path d="M6.6 10.8a15 15 0 0 0 6.6 6.6l2.2-2.2a1 1 0 0 1 1-.25 11 11 0 0 0 3.6.6 1 1 0 0 1 1 1V20a1 1 0 0 1-1 1A17 17 0 0 1 3 4a1 1 0 0 1 1-1h3.5a1 1 0 0 1 1 1 11 11 0 0 0 .6 3.6 1 1 0 0 1-.25 1z"/></symbol>
      <symbol id="icon-mail" viewBox="0 0 24 24"><path d="M2 5h20v14H2z M2 5l10 8 10-8" /><path d="M2 6l10 7 10-7V5H2z" fill="#fff"/></symbol>
      <symbol id="icon-globe" viewBox="0 0 24 24"><path d="M12 2a10 10 0 1 0 0 20 10 10 0 0 0 0-20zm0 2c1 1.3 1.8 3 2.1 5H9.9C10.2 7 11 5.3 12 4zM4.3 11h3.6a17 17 0 0 0 0 2H4.3a8 8 0 0 1 0-2zm5.6 0h4.2a15 15 0 0 1 0 2H9.9a15 15 0 0 1 0-2zm6.2 0h3.6a8 8 0 0 1 0 2h-3.6a17 17 0 0 0 0-2zM9.9 15h4.2c-.3 2-1.1 3.7-2.1 5-1-1.3-1.8-3-2.1-5z"/></symbol>
    </defs>
  </svg>

  <section class="letterhead">
    <div class="brand">Vorbly</div>
    <div class="contacts">
      <span class="contact-item"><svg><use href="#icon-phone"/></svg>(888) 555-0142</span>
      <span class="contact-item"><svg><use href="#icon-mail"/></svg>info@vorbly.com</span>
      <span class="contact-item"><svg><use href="#icon-globe"/></svg>www.vorbly.com</span>
    </div>
    <div class="footer-band">
      <svg viewBox="0 0 566 22" preserveAspectRatio="none">
        <polygon points="0,0 486,0 474,22 0,22" fill="#000"/>
        <polygon points="489,0 566,0 566,22 477,22" fill="#ee1f2a"/>
      </svg>
      <span class="address">48 Harbor Lane, Suite 210, Austin, TX 78701</span>
    </div>
  </section>

  <section class="card card-front">
    <div class="brand">Vorbly</div>
  </section>

  <section class="card card-back">
    <div class="brand">Vorbly</div>
    <div class="person">
      <p class="name">Dana <b>Kessler</b></p>
      <p class="title">President</p>
    </div>
    <p class="address">48 Harbor Lane, Suite 210,<br>Austin, TX 78701</p>
    <div class="details">
      <span class="contact-item"><svg><use href="#icon-phone"/></svg>(888) 555-0142</span>
      <span class="contact-item"><svg><use href="#icon-mail"/></svg>info@vorbly.com</span>
      <span class="contact-item"><svg><use href="#icon-globe"/></svg>www.vorbly.com</span>
    </div>
    <svg class="band" viewBox="0 0 293 10" preserveAspectRatio="none">
      <polygon points="0,0 256,0 251,10 0,10" fill="#000"/>
      <polygon points="259,0 293,0 293,10 254,10" fill="#ee1f2a"/>
    </svg>
  </section>
</body>
</html>
```